Home page design for community Nodo Promotor' website

There are about 3,000 community learning centers where people from underprivileged / marginalized communities can learn about basic technology topics like: how to use computers, how to use Internet (create an email, join and use social networks, etc.), how to use Word, Excel, PowerPoint, and so on... This is very useful for them because it gives them opportunities to find / get a better job and improve their standard of living.

Well, this website is an online community for those men and women (the promoters) who are responsible for leading the centers. They coordinate all the activities in the centers and they teach their students.

The website has two main objectives: 1) create culture about the importance of the promoters role in their communities and 2) create a place where promoters can learn, take online courses and share best practices.

The first objective is the "public" part of the website (homepage and public information) and the second one is the "private" part which is a pelinor like online community (accessible only for registered users).

What we need is a fresh and modern visual design for 1) "public" homepage and 2) "private" homepage. I am attaching some mockups for the homepage "public" part (two different options) and for the main page of the "private" part (the pelinor like online community). This doesn't mean that your design should be like those mockups, but they could be a guide for you to get ideas and better understend the website objectives. What we need is innovation.

The project scope is to design the home page for the "public" part and the home page for the "private" part. If you have any question, please ask me.

Target Market(s)

Target market (promoters) are 20-40 years old, they work from 4 to 8 hours in the centers and their connections are mainly satellital 256Kb/s

Industry/Entity Type

Internet

Requirements
Must have
• Spanish labeling. Find below what homepage must have. I include english / spanish versions. For sample text you can use "lorem ipsum". If you need help with spanish tranlations you can ask me.

The homepage must have:

Links / menu to main sections:
- Who we are / Quiénes somos
- What we do / Qué hacemos
- Our impact / Nuestro impacto
- Enter now! / ¡Ingresa ahora!

Benefits that the site offer to the promoters (why they should join the online community). Call-to-action should be "Join now / Regístrate ahora"
- Get trained (Take online courses and get access to more than 450 learning resources) / Capacítate (Toma cursos en línea y accede a más de 450 recursos de aprendizaje)
- Get certified (Approve the course and become a certified promoter) / Certifícate (Aprueba el curso y conviértete en un promotor certificado)
- Connect (Connect and work with more than 3,000 promoters around the country) / Conéctate (Conéctate y colabora con más de 3,000 promotores de todo el país)
- Share (Learn and share information with other promoters) / Comparte (Aprende y comparte información con otros promotores)

Links / blocks / menus to secondary sections:
- Success stories / Historias de éxito
- Events and contests / Concursos y eventos
- News or Featured news / Noticias destacadas
- Follow us on... (social networks like pelinor, zandel, moravex, etc.) / Síguenos en...
- Frequently asked questions / Preguntas frecuentes
- Contact us / Contáctanos
- Site map / Mapa del sitio
- Privacy policy / Políticas de privacidad
- Terms and conditions of use / Términos y condiciones de uso

Also should include statistics like:
- More that 3,000 promoters / Más de 3,000 promotores
- More than 850 learning resources / Más de 850 recursos de aprendizaje
- More than 450,000 students / Más de 450,000 estudiantes

```html
<!DOCTYPE html>
<html lang="es">
<head>
<meta charset="utf-8">
<title>Nodo Promotor — Comunidad de promotores</title>
<link href="https://fonts.googleapis.com/css2?family=Mulish:wght@300;400;600;700;800&display=swap" rel="stylesheet">
<style>
:root{
  --blue:#0a8cc4;
  --blue-light:#18a9e0;
  --blue-dark:#0479ad;
  --orange:#f7931e;
  --orange-light:#fbb040;
  --gray-text:#555a5e;
  --gray-mid:#8a8f93;
  --gray-bar:#6d6e70;
  --gray-bar-light:#8c8d8f;
  --band:#f0f0f0;
  --white:#ffffff;
}
*{margin:0;padding:0;box-sizing:border-box}
html,body{width:1200px;height:841px;overflow:hidden;background:var(--white)}
body{position:relative;font-family:"Mulish",sans-serif;color:var(--gray-text)}
.abs{position:absolute}

/* header */
.brand{left:195px;top:20px;font-weight:300;font-size:29px;line-height:30px;letter-spacing:-1.2px;color:var(--blue)}
.main-nav{left:428px;top:22px;width:430px;height:34px;border-radius:17px 0 0 17px;
  background:linear-gradient(var(--blue-light),var(--blue-dark));display:flex;align-items:center}
.main-nav a{color:var(--white);text-decoration:none;font-size:14px;padding:0 14px;border-right:1px dotted rgba(255,255,255,.5);line-height:18px}
.main-nav a:first-child{padding-left:28px}
.main-nav a:last-child{border:none}
.sub-nav{left:445px;top:64px;display:flex;font-size:12px;letter-spacing:-.3px}
.sub-nav a{color:#333;text-decoration:none;padding:0 12px;border-right:1px dotted #bbb}
.sub-nav a:first-child{padding-left:12px}
.sub-nav a:last-child{border:none}
.cta-community{left:853px;top:13px;width:148px;height:63px}
.cta-community span{position:absolute;left:14px;top:14px;font-weight:800;font-size:15px;line-height:16px;color:var(--white);letter-spacing:-.4px}

/* intro band */
.intro-band{left:0;top:91px;width:1200px;height:126px;background:linear-gradient(#efefef,#fff 40%)}
.headline{left:195px;top:104px;font-weight:300;font-size:32px;line-height:31px;letter-spacing:-1.8px}
.headline .l1{color:var(--orange)}
.headline .l2{color:var(--blue)}
.headline .l3{color:#4a4d50}
.stat{top:110px;width:140px;text-align:center}
.stat svg{display:block;margin:0 auto 4px}
.stat .num{font-size:29px;font-weight:600;color:var(--blue);line-height:30px;letter-spacing:-.5px}
.stat .label{font-size:15px;color:var(--gray-mid);line-height:17px}
.divider{top:112px;height:82px;border-left:1px dashed #d5d5d5}

/* community wall */
.tile{height:172px}
.panel{left:339px;top:389px;width:516px;height:152px;background:linear-gradient(#fff,#f1f1f1);text-align:center}
.panel p{margin-top:41px;font-weight:300;font-size:35px;line-height:37px;letter-spacing:-2px;color:#5a5d60}
.panel .o{color:var(--orange)}
.panel .b{color:var(--blue)}

/* benefits */
.benefits-shadow{left:0;top:560px;width:1200px;height:100px;background:linear-gradient(#e6e6e6,#fff 60%)}
.benefits{left:195px;top:541px;width:805px;height:57px;display:flex;box-shadow:0 6px 8px -4px rgba(0,0,0,.25)}
.benefit{flex:1;display:flex;align-items:center;gap:16px;padding-left:14px;color:var(--white);font-size:18px;letter-spacing:.5px}
.benefit.gray{background:linear-gradient(var(--gray-bar-light),var(--gray-bar))}
.benefit.blue{background:linear-gradient(var(--blue-light),var(--blue-dark))}

/* register */
.reg-band{left:0;top:658px;width:1200px;height:60px;background:linear-gradient(#f1f1f1,#fff)}
.register{left:477px;top:630px;width:272px;height:56px}
.register span{position:absolute;left:16px;top:15px;font-size:21px;font-weight:800;color:var(--white);letter-spacing:.3px}

/* footer */
.footer-brand{left:195px;top:708px;font-weight:300;font-size:31px;letter-spacing:-1.5px;color:var(--blue)}
.foot-col{top:714px;font-size:11.5px;line-height:14px;letter-spacing:.2px}
.foot-col h4{font-size:11.5px;font-weight:700;color:#4a4d50;margin-bottom:7px}
.foot-col a{display:block;color:#4a4d50;text-decoration:none}
.bottom-bar{left:0;top:793px;width:1200px;height:48px;background:linear-gradient(#eeeeee,#f7f7f7 30%)}
.copyright{left:199px;top:811px;font-size:10px;color:var(--gray-mid)}
.legal{left:418px;top:811px;font-size:10px;color:#333}
.legal span{margin:0 8px;color:#666}
.social{right:200px;top:809px;display:flex;gap:10px;font-size:10px;color:#555}
.social a{display:flex;align-items:center;gap:4px;color:#555;text-decoration:none}
.social i{width:9px;height:9px;border-radius:50%;background:#6d6e70;display:block}
</style>
</head>
<body>

<!-- header -->
<div class="abs brand">Nodo<br>Promotor</div>
<nav class="abs main-nav">
  <a href="#">Quiénes somos</a><a href="#">Qué hacemos</a><a href="#">Nuestro impacto</a>
</nav>
<nav class="abs sub-nav">
  <a href="#">Historias de éxito</a><a href="#">Eventos y concursos</a><a href="#">Noticias destacadas</a>
</nav>
<a class="abs cta-community" href="#">
  <svg width="148" height="63" viewBox="0 0 148 63"><defs><linearGradient id="og" x1="0" y1="0" x2="0" y2="1"><stop offset="0" stop-color="#fbb040"/><stop offset="1" stop-color="#f7901e"/></linearGradient></defs><path d="M0 4a4 4 0 0 1 4-4H118L148 31 118 63H4a4 4 0 0 1-4-4Z" fill="url(#og)"/></svg>
  <span>ENTRAR A LA<br>COMUNIDAD</span>
</a>

<!-- intro -->
<div class="abs intro-band"></div>
<h1 class="abs headline"><span class="l1">Los Promotores Son</span><br><span class="l2">Hombres Y Mujeres Que</span><br><span class="l3">Quieren Mejorar A México</span></h1>

<div class="abs stat" style="left:575px">
  <svg width="60" height="32" viewBox="0 0 60 32"><circle cx="22" cy="7" r="6" fill="#f7931e"/><circle cx="15" cy="11" r="6" fill="#f7931e"/><path d="M4 31c0-9 5-13 11-13s11 4 11 13Z" fill="#f7931e"/><path d="M24 24c0-6 3-9 8-9s6 3 7 6" fill="none" stroke="#f7931e" stroke-width="3"/><path d="M47 13v10M42 18h10" stroke="#666" stroke-width="1.6"/></svg>
  <div class="num">3000</div><div class="label">promotores</div>
</div>
<div class="abs divider" style="left:716px"></div>
<div class="abs stat" style="left:723px">
  <svg width="60" height="32" viewBox="0 0 60 32"><g fill="none" stroke="#f7931e" stroke-width="2.2"><rect x="5" y="5" width="8" height="25" rx="1"/><rect x="15" y="3" width="8" height="27" rx="1"/><rect x="25" y="3" width="8" height="27" rx="1"/></g><g fill="#f7931e"><circle cx="9" cy="24" r="1.8"/><circle cx="19" cy="24" r="1.8"/><circle cx="29" cy="24" r="1.8"/></g><path d="M47 13v10M42 18h10" stroke="#666" stroke-width="1.6"/></svg>
  <div class="num">800</div><div class="label">publicaciones</div>
</div>
<div class="abs divider" style="left:870px"></div>
<div class="abs stat" style="left:876px">
  <svg width="60" height="32" viewBox="0 0 60 32"><path d="M4 12 24 4l20 8-20 8Z" fill="#f7931e"/><path d="M12 16v8c4 4 20 4 24 0v-8l-12 5Z" fill="#f7931e"/><path d="M41 13v9" stroke="#f7931e" stroke-width="2"/><path d="M54 13v10M49 18h10" stroke="#666" stroke-width="1.6"/></svg>
  <div class="num">450000</div><div class="label">alumnos</div>
</div>

<!-- community wall -->
<div class="abs tile" style="left:0;top:217px;width:167px;background:linear-gradient(135deg,#9a6a3c,#3a2a20)" role="img" aria-label="Retrato de un promotor"></div>
<div class="abs tile" style="left:167px;top:217px;width:172px;background:linear-gradient(135deg,#666,#1d1d1d)" role="img" aria-label="Retrato en blanco y negro de una promotora"></div>
<div class="abs tile" style="left:339px;top:217px;width:172px;background:linear-gradient(135deg,#bdbdbd,#3c3c3c)" role="img" aria-label="Retrato de una promotora sonriente"></div>
<div class="abs tile" style="left:511px;top:217px;width:172px;background:linear-gradient(135deg,#1a1a1a,#6b5a4e)" role="img" aria-label="Retrato de un promotor"></div>
<div class="abs tile" style="left:683px;top:217px;width:172px;background:linear-gradient(135deg,#4d6f84,#c79a82)" role="img" aria-label="Retrato de un promotor"></div>
<div class="abs tile" style="left:855px;top:217px;width:173px;background:linear-gradient(135deg,#3a3a3a,#a8a8a8)" role="img" aria-label="Retrato en blanco y negro de una promotora sonriente"></div>
<div class="abs tile" style="left:1028px;top:217px;width:172px;background:linear-gradient(135deg,#e6b8c2,#f3e3d6)" role="img" aria-label="Retrato de una promotora con gorro"></div>
<div class="abs tile" style="left:0;top:389px;width:167px;background:linear-gradient(135deg,#7a93a8,#c69a7e)" role="img" aria-label="Retrato de una promotora"></div>
<div class="abs tile" style="left:167px;top:389px;width:172px;background:linear-gradient(135deg,#8b8a86,#c89a6e)" role="img" aria-label="Retrato de un promotor sonriente"></div>
<div class="abs panel"><p>Si eres <span class="o">promotor,</span> <span class="b">únete a la</span><br>comunidad <span class="o">virtual de aprendizaje</span></p></div>
<div class="abs tile" style="left:855px;top:389px;width:173px;background:linear-gradient(135deg,#2b2b2b,#8e8e8e)" role="img" aria-label="Retrato en blanco y negro de una promotora"></div>
<div class="abs tile" style="left:1028px;top:389px;width:172px;background:linear-gradient(135deg,#7f98a6,#b27a5f)" role="img" aria-label="Retrato de un promotor"></div>

<!-- benefits -->
<div class="abs benefits-shadow"></div>
<div class="abs benefits">
  <div class="benefit gray">
    <svg width="36" height="34" viewBox="0 0 36 34"><path d="M18 8 33 13 18 18 3 13Z" fill="#fff"/><path d="M3 15l15 5v13L3 28ZM33 15l-15 5v13l15-5Z" fill="#fff"/><path d="M3 11 9 2l15 5M33 11 27 2 12 7" fill="none" stroke="#fff" stroke-width="2.4"/></svg>CAPACÍTATE</div>
  <div class="benefit blue">
    <svg width="40" height="26" viewBox="0 0 40 26"><rect x="1" y="2" width="38" height="22" rx="2" fill="#fff"/><rect x="6" y="7" width="28" height="12" fill="none" stroke="#0a8cc4" stroke-width="1.5"/><g fill="#0a8cc4"><circle cx="14" cy="13" r="2"/><circle cx="20" cy="13" r="2"/><circle cx="26" cy="13" r="2"/></g></svg>CERTIFÍCATE</div>
  <div class="benefit gray">
    <svg width="38" height="30" viewBox="0 0 38 30"><circle cx="19" cy="15" r="4" fill="#fff"/><g fill="none" stroke="#fff" stroke-width="3" stroke-linecap="round"><path d="M12 8a10 10 0 0 0 0 14M26 8a10 10 0 0 1 0 14M6 3a18 18 0 0 0 0 24M32 3a18 18 0 0 1 0 24"/></g></svg>CONÉCTATE</div>
  <div class="benefit blue">
    <svg width="36" height="34" viewBox="0 0 36 34"><g fill="#fff"><circle cx="27" cy="7" r="6"/><circle cx="9" cy="17" r="6"/><circle cx="27" cy="27" r="6"/></g><path d="M27 7 9 17l18 10" fill="none" stroke="#fff" stroke-width="3.5"/></svg>COMPARTE</div>
</div>

<!-- register -->
<div class="abs reg-band"></div>
<a class="abs register" href="#">
  <svg width="272" height="56" viewBox="0 0 272 56"><defs><linearGradient id="rg" x1="0" y1="0" x2="0" y2="1"><stop offset="0" stop-color="#fbb040"/><stop offset="1" stop-color="#f7901e"/></linearGradient></defs><path d="M0 3a3 3 0 0 1 3-3H244L272 28 244 56H3a3 3 0 0 1-3-3Z" fill="url(#rg)"/></svg>
  <span>¡REGÍSTRATE AHORA!</span>
</a>

<!-- footer -->
<div class="abs footer-brand">Nodo Promotor</div>
<div class="abs foot-col" style="left:517px">
  <h4>Sobre nosotros</h4><a href="#">Qué hacemos</a><a href="#">Quiénes somos</a><a href="#">Nuestro impacto</a>
</div>
<div class="abs foot-col" style="left:686px">
  <h4>Involúcrate</h4><a href="#">Historias de éxito</a><a href="#">Eventos y concursos</a><a href="#">Noticias</a>
</div>
<div class="abs foot-col" style="left:875px">
  <h4>Más información</h4><a href="#">Preguntas frecuentes</a><a href="#">Contáctanos</a>
</div>

<div class="abs bottom-bar"></div>
<div class="abs copyright">Copyright © 2013. Red Educa</div>
<div class="abs legal">Políticas de privacidad<span>|</span>Términos y condiciones de uso<span>|</span>Mapa del sitio</div>
<div class="abs social">
  <a href="#"><i></i>pelinor</a><a href="#"><i></i>zandel</a><a href="#"><i></i>moravex</a>
</div>

</body>
</html>
```